Fernwick Ridge Glide Treks

We offer guided cross country ( Nordic ) skiing tours in the National Forest bordering Yellowstone National Park. I need a website that attracts individuals by using photos ( provided by me ) , brief descriptions of what to expect, a place with phone numbers to call for a tour, and I would like the website to feature the same color scheme as the logo, which I will upload.

```html
<!DOCTYPE html>
<html lang="en">
<head>
<meta charset="utf-8">
<title>Fernwick Ridge Glide Treks — Website Design</title>
<link href="https://fonts.googleapis.com/css2?family=Barlow:wght@400;500&family=Oswald:wght@400;500&display=swap" rel="stylesheet">
<style>
:root{
  --board:#cfd9ec;
  --blue:#7b95d2;
  --blue-soft:#9db0e0;
  --blue-deep:#6a82bb;
  --bar:#c6d3ee;
  --ice:#f5f5f7;
  --tint:#eef2fa;
  --ink:#1f2430;
  --muted:#7d8394;
  --white:#ffffff;
}
*{margin:0;padding:0;box-sizing:border-box}
html,body{width:1200px;height:3726px;overflow:hidden}
body{background:var(--board);position:relative;font-family:"Barlow",sans-serif;color:var(--ink)}
.abs{position:absolute}
.center{left:0;right:0;text-align:center}
.head{font-family:"Oswald",sans-serif;font-weight:500;text-transform:uppercase;color:var(--ink);line-height:1.2}
.kicker{font-family:"Barlow",sans-serif;text-transform:uppercase;letter-spacing:3px;color:var(--blue-soft)}
.copy{color:var(--muted);line-height:1.75}
.btn{background:var(--blue);color:var(--white);font-family:"Oswald",sans-serif;text-transform:uppercase;display:flex;align-items:center;justify-content:center}
.photo{position:absolute}

/* board header */
.brand-mark{left:330px;top:102px;width:120px;height:120px;border-radius:50%;border:2px solid var(--ink);display:flex;align-items:center;justify-content:center;text-align:center;font-family:"Oswald",sans-serif;font-size:13px;line-height:1.3;text-transform:uppercase;color:var(--ink);padding:14px}
.rule{width:1px;height:82px;background:#aab7d4;top:118px}
.spec-title{font-family:"Barlow",sans-serif;font-size:21px;color:#3d4358}
.swatch{width:38px;height:38px;border-radius:50%;top:147px}
.hex{font-size:8px;color:#59617a;top:192px}

/* flat screen previews */
.screen{background:var(--white);overflow:hidden}
.screen .s-top{position:absolute;left:0;right:0;top:0;background:var(--bar)}
.screen .s-hero{position:absolute;left:0;right:0;bottom:0;background:linear-gradient(160deg,#8a8f98 0%,#c9ccd2 40%,#6f747d 70%,#dfe2e6 100%)}

/* desktop page */
.desk{left:153px;top:856px;width:668px;height:2764px;background:var(--white);overflow:hidden}
.m{left:948px;top:856px;width:151px;height:2764px;background:var(--white);overflow:hidden}
.sec{position:absolute;left:0;right:0}
.topbar{background:var(--bar);font-size:6.5px;color:#4b5370}
.soc{display:inline-block;width:5px;height:5px;border-radius:50%;background:var(--blue);margin-left:4px}
.logo-lockup{display:flex;align-items:center;gap:6px;font-family:"Oswald",sans-serif;font-size:7.5px;line-height:1.2;text-transform:uppercase;color:var(--ink)}
.logo-dot{border-radius:50%;border:1.5px solid var(--ink);flex:none}
.menu{display:flex;gap:26px;font-size:7px;color:#3d4358}
.menu .on{color:var(--blue)}
.hero-photo{background:linear-gradient(170deg,#6b7079 0%,#b9bdc4 30%,#7f848c 55%,#d8dbe0 80%,#eceef1 100%)}
.hero-shade{background:rgba(30,34,40,.35)}
.hero-sub{color:#f1f3f7;letter-spacing:2.4px;text-transform:uppercase}
.hero-title{font-family:"Oswald",sans-serif;font-weight:500;text-transform:uppercase;color:var(--white)}
.round-photo{border-radius:50%;border:3px solid var(--white);box-shadow:0 0 0 1px #d9dfee;background:linear-gradient(180deg,#8fa6d4 0%,#dfe6f3 45%,#f7f8fb 70%,#c7cfdc 100%)}
.feat{display:flex;flex-direction:column;gap:4px;font-size:6px;text-transform:uppercase;color:var(--blue-soft);line-height:1.3}
.feat svg{display:block}
.card-img{background:linear-gradient(180deg,#a9b8d6 0%,#e6ebf3 45%,#7c8aa3 100%)}
.card-label{background:var(--blue);color:var(--white);font-family:"Oswald",sans-serif;text-transform:uppercase;display:flex;align-items:center;justify-content:center}
.book{background:linear-gradient(100deg,#b8c8e9 0%,#c7d4ee 45%,#e6ebf4 75%,#d4dbe6 100%)}
.book .head{color:var(--white)}
.book .copy{color:#f3f5fb}
.g1{background:linear-gradient(180deg,#5f6570,#c9ced6 55%,#414852)}
.g2{background:linear-gradient(180deg,#c5d2e6,#eef1f5 40%,#8b96a4)}
.g3{background:linear-gradient(180deg,#9eb6e6,#dfe8f6 60%,#f7f9fc)}
.g4{background:linear-gradient(180deg,#dfe7f3,#9fb3d3 70%,#6d86b3)}
.g5{background:linear-gradient(135deg,#6d8ac4,#b8c9e8 50%,#5a78b4)}
.call{background:linear-gradient(180deg,#7089c2,#6580b8)}
.call .head{color:var(--white)}
.call .copy{color:#e3e9f6}
.testi{background:var(--tint)}
.avatar{border-radius:50%;background:linear-gradient(180deg,#d9c2b0,#b99784)}
.name{color:var(--blue);font-size:6.5px}
.save{background:linear-gradient(180deg,#ffffff 0%,#ffffff 60%,#f0f3f8 80%,#e6eaf2 100%)}
.footer{background:var(--tint)}
.contact{display:flex;justify-content:center;gap:18px;font-size:6px;color:#4b5370;align-items:center}
.contact svg{margin-right:4px;vertical-align:middle}
.socials{display:flex;justify-content:center;gap:7px}
.socials span{width:9px;height:9px;background:#d5def1}
.socials span.on{background:var(--blue)}
.copyright{background:var(--bar);font-size:5.5px;color:#4b5370;display:flex;align-items:center;justify-content:center}

.side-label{font-family:"Barlow",sans-serif;font-size:19px;letter-spacing:9px;color:var(--blue);transform:rotate(-90deg);transform-origin:left top;white-space:nowrap}
</style>
</head>
<body>

<!-- board header -->
<div class="abs brand-mark">Fernwick Ridge<br>Glide Treks</div>
<div class="abs rule" style="left:528px"></div>
<div class="abs spec-title" style="left:604px;top:116px">Fonts:</div>
<div class="abs" style="left:604px;top:154px;font-family:'Oswald',sans-serif;font-size:19px;color:var(--blue)">Oswald</div>
<div class="abs" style="left:604px;top:180px;font-size:16px;color:var(--blue-soft)">Barlow</div>
<div class="abs rule" style="left:740px"></div>
<div class="abs spec-title" style="left:817px;top:116px">Colors:</div>
<div class="abs swatch" style="left:817px;background:var(--blue)"></div>
<div class="abs swatch" style="left:864px;background:var(--blue-soft)"></div>
<div class="abs swatch" style="left:909px;background:var(--ice)"></div>
<div class="abs hex" style="left:818px">#7b95d2</div>
<div class="abs hex" style="left:865px">#9db0e0</div>
<div class="abs hex" style="left:911px">#f5f5f7</div>

<!-- flat screen previews -->
<div class="abs screen" style="left:353px;top:304px;width:587px;height:329px">
  <div class="s-top" style="height:12px"></div>
  <div class="abs" style="left:84px;top:22px;width:26px;height:26px;border-radius:50%;border:1.5px solid var(--ink)"></div>
  <div class="abs menu" style="right:76px;top:33px;font-size:5.5px;gap:20px"><span class="on">Home</span><span>About Us</span><span>Tours</span><span>Contact</span></div>
  <div class="s-hero hero-photo" role="img" aria-label="Snowy pine forest trail with a cross-country skier" style="top:56px"></div>
  <div class="abs center hero-sub" style="top:190px;font-size:6px">Skiing tours in the national forest bordering Yellowstone National Park</div>
  <div class="abs center hero-title" style="top:235px;font-size:18px">Go for a tour in some the best Nordic places</div>
  <div class="abs btn" style="left:270px;top:294px;width:62px;height:20px;font-size:5.5px">Book Tour</div>
</div>
<div class="abs screen" style="left:159px;top:544px;width:372px;height:211px">
  <div class="s-top" style="height:8px"></div>
  <div class="abs" style="left:52px;top:14px;width:18px;height:18px;border-radius:50%;border:1px solid var(--ink)"></div>
  <div class="abs menu" style="right:48px;top:21px;font-size:4px;gap:12px"><span class="on">Home</span><span>About Us</span><span>Tours</span><span>Contact</span></div>
  <div class="s-hero hero-photo" role="img" aria-label="Snowy pine forest trail with a cross-country skier" style="top:37px"></div>
  <div class="abs center hero-sub" style="top:116px;font-size:4px">Skiing tours in the national forest bordering Yellowstone National Park</div>
  <div class="abs center hero-title" style="top:144px;font-size:11px">Go for a tour in some the best Nordic places</div>
  <div class="abs btn" style="left:170px;top:184px;width:34px;height:12px;font-size:3.5px">Book Tour</div>
</div>
<div class="abs screen" style="left:966px;top:552px;width:120px;height:233px">
  <div class="s-top" style="height:8px"></div>
  <div class="abs" style="left:8px;top:12px;width:18px;height:18px;border-radius:50%;border:1px solid var(--ink)"></div>
  <div class="s-hero hero-photo" role="img" aria-label="Snowy pine forest trail with a cross-country skier" style="top:36px"></div>
  <div class="abs center hero-title" style="top:133px;font-size:8.5px;padding:0 8px">Go for a tour in some the best Nordic places</div>
  <div class="abs btn" style="left:42px;top:176px;width:36px;height:11px;font-size:3.5px">Book Tour</div>
</div>

<div class="abs side-label" style="left:108px;top:1829px">LAPTOP / DESKTOP</div>
<div class="abs side-label" style="left:905px;top:1714px">MOBILE</div>

<!-- ================= DESKTOP ================= -->
<main class="abs desk">
  <div class="sec topbar" style="top:0;height:17px">
    <span class="abs" style="left:88px;top:5px">hello@fernwickridge.test</span>
    <span class="abs" style="right:88px;top:5px"><i class="soc"></i><i class="soc"></i></span>
  </div>
  <header class="sec" style="top:17px;height:63px">
    <div class="abs logo-lockup" style="left:88px;top:13px"><span class="logo-dot" style="width:36px;height:36px"></span><span>Fernwick Ridge<br>Glide Treks</span></div>
    <nav class="abs menu" style="right:89px;top:27px"><span class="on">Home</span><span>About Us</span><span>Tours</span><span>Contact</span></nav>
  </header>

  <section class="sec" style="top:80px;height:419px">
    <div class="photo hero-photo" role="img" aria-label="Snow-laden pine forest with a skier on a trail" style="inset:0"></div>
    <div class="photo hero-shade" style="inset:0"></div>
    <p class="abs center hero-sub" style="top:135px;font-size:7px">Skiing tours in the national forest bordering Yellowstone National Park</p>
    <h1 class="abs center hero-title" style="top:185px;font-size:24px">Go for a tour in some the best Nordic places</h1>
    <div class="abs btn" style="left:311px;top:256px;width:71px;height:27px;font-size:7px">Book Tour</div>
  </section>

  <section class="sec" style="top:499px;height:333px">
    <div class="photo round-photo" role="img" aria-label="Skiers climbing a snowy mountain slope" style="left:90px;top:65px;width:202px;height:202px"></div>
    <p class="abs kicker" style="left:340px;top:48px;font-size:6px">Introduction</p>
    <h2 class="abs head" style="left:340px;top:60px;font-size:19px">About Fernwick Ridge<br>Glide Treks</h2>
    <p class="abs copy" style="left:340px;top:136px;width:245px;font-size:6.3px">Lorem ipsum dolor sit amet, consectetur adipiscing elit, sed do eiusmod tempor incididunt ut labore et dolore magna aliqua. Quis ipsum suspendisse ultrices gravida.</p>
    <div class="abs" style="left:340px;top:186px;display:flex;gap:52px">
      <div class="feat"><svg width="18" height="14" viewBox="0 0 18 14"><path d="M1 13 L17 9 M5 11 L9 3 L13 10" fill="none" stroke="#9db0e0" stroke-width="1.2"/><circle cx="9" cy="2" r="1.4" fill="#9db0e0"/></svg>Professional<br>team</div>
      <div class="feat"><svg width="18" height="14" viewBox="0 0 18 14"><path d="M1 13 L17 9 M5 11 L9 3 L13 10" fill="none" stroke="#9db0e0" stroke-width="1.2"/><circle cx="9" cy="2" r="1.4" fill="#9db0e0"/></svg>Certified<br>instructors</div>
      <div class="feat"><svg width="18" height="14" viewBox="0 0 18 14"><path d="M1 13 L17 9 M5 11 L9 3 L13 10" fill="none" stroke="#9db0e0" stroke-width="1.2"/><circle cx="9" cy="2" r="1.4" fill="#9db0e0"/></svg>Affordable<br>pricing</div>
    </div>
    <p class="abs copy" style="left:340px;top:246px;width:245px;font-size:6.3px">Lorem ipsum dolor sit amet, consectetur adipiscing elit, sed do eiusmod tempor incididunt ut labore et dolore magna aliqua. Quis ipsum suspendisse ultrices gravida.</p>
  </section>

  <section class="sec testi" style="top:832px;height:344px">
    <p class="abs center kicker" style="top:49px;font-size:6px">Places to visit</p>
    <h2 class="abs center head" style="top:62px;font-size:19px">Tour skiing places</h2>
    <p class="abs copy" style="left:140px;width:388px;top:106px;font-size:6.3px;text-align:center">Lorem ipsum dolor sit amet, consectetur adipiscing elit, sed do eiusmod tempor incididunt ut labore et dolore magna aliqua. Quis ipsum suspendisse ultrices gravida. Risus commodo viverra maecenas accumsan lacus vel facilisis.</p>
    <div class="photo card-img" role="img" aria-label="Snowy forest at Castle" style="left:88px;top:156px;width:155px;height:118px"></div>
    <div class="abs card-label" style="left:98px;top:254px;width:135px;height:36px;font-size:8px">Castle</div>
    <div class="photo card-img" role="img" aria-label="Snow-capped Electric Peak" style="left:256px;top:156px;width:155px;height:118px;background:linear-gradient(180deg,#4d7cc9 0%,#a9c2ea 40%,#eef2f8 70%,#b6c3d6 100%)"></div>
    <div class="abs card-label" style="left:266px;top:254px;width:135px;height:36px;font-size:8px">Electric Peak</div>
    <div class="photo card-img" role="img" aria-label="Forest trail at Mineral Hill" style="left:424px;top:156px;width:155px;height:118px;background:linear-gradient(180deg,#9fb7e2 0%,#4d5a4f 40%,#e8ecf2 85%)"></div>
    <div class="abs card-label" style="left:434px;top:254px;width:135px;height:36px;font-size:8px">Mineral Hi</div>
  </section>

  <section class="sec book" role="img" aria-label="Snow-covered spruce trees on a white hillside" style="top:1176px;height:298px">
    <h2 class="abs head" style="left:88px;top:48px;font-size:19px;font-weight:400">Book your tour now and<br>have an amazing experience</h2>
    <p class="abs copy" style="left:88px;top:118px;width:285px;font-size:6px">Lorem ipsum dolor sit amet, consectetur adipiscing elit, sed do eiusmod tempor incididunt ut labore et dolore magna aliqua. Quis ipsum suspendisse ultrices gravida. Risus commodo viverra maecenas accumsan lacus.</p>
    <p class="abs copy" style="left:88px;top:166px;width:285px;font-size:6px">Lorem ipsum dolor sit amet, consectetur adipiscing elit, sed do eiusmod tempor incididunt ut labore et dolore magna aliqua.</p>
    <div class="abs btn" style="left:88px;top:218px;width:71px;height:29px;font-size:6.5px">Book Tour</div>
  </section>

  <section class="sec" style="top:1474px;height:381px">
    <p class="abs center kicker" style="top:49px;font-size:6px">Recent posts</p>
    <h2 class="abs center head" style="top:62px;font-size:19px">Gallery</h2>
    <div class="photo g1" role="img" aria-label="Dark pines against misty light" style="left:88px;top:110px;width:154px;height:102px"></div>
    <div class="photo g2" role="img" aria-label="Tall snowy pines beside a trail" style="left:251px;top:110px;width:154px;height:220px"></div>
    <div class="photo g3" role="img" aria-label="Frosted trees on an open snowfield" style="left:424px;top:110px;width:155px;height:102px"></div>
    <div class="photo g4" role="img" aria-label="Foggy blue winter forest" style="left:88px;top:227px;width:154px;height:103px"></div>
    <div class="photo g5" role="img" aria-label="Aerial view of a road through snowy forest" style="left:424px;top:227px;width:155px;height:103px"></div>
  </section>

  <section class="sec call" style="top:1855px;height:193px">
    <h2 class="abs center head" style="top:46px;font-size:20px;font-weight:400">Call us now at<br>+1 234 567 890</h2>
    <p class="abs copy" style="left:214px;width:240px;top:120px;font-size:6px;text-align:center">Lorem ipsum dolor sit amet, consectetur adipiscing elit, sed do eiusmod tempor incididunt ut labore et dolore magna aliqua.</p>
  </section>

  <section class="sec testi" style="top:2048px;height:253px">
    <p class="abs center kicker" style="top:49px;font-size:6px">What our clients say</p>
    <h2 class="abs center head" style="top:62px;font-size:19px">Testimonials</h2>
    <div class="abs" style="left:88px;top:112px;width:491px;display:flex;justify-content:space-between">
      <div style="width:155px;text-align:center"><p class="copy" style="font-size:6px">Lorem ipsum dolor sit amet, consectetur et nisl adipiscing elit, sed do eiusmod tempor incididunt ut labore et dolore magna aliqua.</p><div class="avatar" role="img" aria-label="Client portrait" style="width:22px;height:22px;margin:16px auto 6px"></div><p class="name">Dana Holloway</p></div>
      <div style="width:155px;text-align:center"><p class="copy" style="font-size:6px">Lorem ipsum dolor sit amet, consectetur et nisl adipiscing elit, sed do eiusmod tempor incididunt ut labore et dolore magna aliqua.</p><div class="avatar" role="img" aria-label="Client portrait" style="width:22px;height:22px;margin:16px auto 6px"></div><p class="name">Dana Holloway</p></div>
      <div style="width:155px;text-align:center"><p class="copy" style="font-size:6px">Lorem ipsum dolor sit amet, consectetur et nisl adipiscing elit, sed do eiusmod tempor incididunt ut labore et dolore magna aliqua.</p><div class="avatar" role="img" aria-label="Client portrait" style="width:22px;height:22px;margin:16px auto 6px"></div><p class="name">Dana Holloway</p></div>
    </div>
  </section>

  <section class="sec save" style="top:2301px;height:263px">
    <h2 class="abs center head" style="top:56px;font-size:19px">Save up to 30% at early winter</h2>
    <p class="abs copy" style="left:214px;width:240px;top:94px;font-size:6px;text-align:center">Lorem ipsum dolor sit amet, consectetur adipiscing elit, sed do eiusmod tempor incididunt ut labore et dolore magna aliqua.</p>
    <div class="abs btn" style="left:299px;top:143px;width:70px;height:26px;font-size:6.5px">Learn More</div>
  </section>

  <footer class="sec footer" style="top:2564px;height:181px">
    <div class="abs logo-lockup" style="left:0;right:0;top:10px;justify-content:center"><span class="logo-dot" style="width:40px;height:40px"></span><span>Fernwick Ridge<br>Glide Treks</span></div>
    <div class="abs contact" style="left:0;right:0;top:83px">
      <span><svg width="7" height="7" viewBox="0 0 10 10"><path d="M2 1 L4 1 L5 3.5 L3.8 4.5 Q5 6.5 6.5 6.7 L7.5 5.5 L10 6.5 L10 8.5 Q9 10 7 9.5 Q1 7.5 0.5 2 Q0.8 1 2 1Z" fill="#4b5370"/></svg>+1 234 567 890</span>
      <span><svg width="8" height="6" viewBox="0 0 12 9"><rect x=".5" y=".5" width="11" height="8" fill="none" stroke="#4b5370"/><path d="M.5 .5 L6 5 L11.5 .5" fill="none" stroke="#4b5370"/></svg>hello@fernwickridge.test</span>
    </div>
    <div class="abs socials" style="left:0;right:0;top:117px"><span></span><span class="on"></span><span></span></div>
  </footer>
  <div class="sec copyright" style="top:2745px;height:19px">Copyright 2021 © Fernwick Ridge Glide Treks - All rights reserved</div>
</main>

<!-- ================= MOBILE ================= -->
<main class="abs m">
  <div class="sec topbar" style="top:0;height:12px;font-size:4px">
    <span class="abs" style="left:9px;top:4px">hello@fernwickridge.test</span>
    <span class="abs" style="right:9px;top:3px"><i class="soc" style="width:4px;height:4px;margin-left:2px"></i><i class="soc" style="width:4px;height:4px;margin-left:2px"></i></span>
  </div>
  <header class="sec" style="top:12px;height:39px">
    <span class="abs logo-dot" style="left:9px;top:7px;width:24px;height:24px"></span>
    <svg class="abs" style="right:10px;top:16px" width="9" height="7" viewBox="0 0 9 7"><path d="M0 .5H9M0 3.5H9M0 6.5H9" stroke="#7b95d2"/></svg>
  </header>
  <section class="sec" style="top:51px;height:269px">
    <div class="photo hero-photo" role="img" aria-label="Snow-laden pine forest with a skier on a trail" style="inset:0"></div>
    <div class="photo hero-shade" style="inset:0"></div>
    <p class="abs center hero-sub" style="top:80px;font-size:4px;letter-spacing:1px;padding:0 16px;line-height:1.6">Skiing tours in the national forest bordering Yellowstone National Park</p>
    <h1 class="abs center hero-title" style="top:112px;font-size:11px;line-height:1.3;padding:0 8px">Go for a tour in some the best Nordic places</h1>
    <div class="abs btn" style="left:56px;top:170px;width:39px;height:12px;font-size:3.5px">Book Tour</div>
  </section>

  <section class="sec" style="top:320px;height:397px">
    <div class="photo round-photo" role="img" aria-label="Skiers climbing a snowy mountain slope" style="left:16px;top:38px;width:118px;height:118px"></div>
    <p class="abs kicker" style="left:12px;top:182px;font-size:4px;letter-spacing:1.5px">Introduction</p>
    <h2 class="abs head" style="left:12px;top:192px;font-size:11px">About Fernwick Ridge<br>Glide Treks</h2>
    <p class="abs copy" style="left:12px;width:128px;top:237px;font-size:4px">Lorem ipsum dolor sit amet, consectetur adipiscing elit, sed do eiusmod tempor incididunt ut labore et dolore magna aliqua. Quis ipsum suspendisse ultrices.</p>
    <div class="abs" style="left:12px;top:288px;display:flex;gap:22px">
      <div class="feat" style="font-size:3.5px"><svg width="12" height="10" viewBox="0 0 18 14"><path d="M1 13 L17 9 M5 11 L9 3 L13 10" fill="none" stroke="#9db0e0" stroke-width="1.4"/><circle cx="9" cy="2" r="1.6" fill="#9db0e0"/></svg>Professional<br>team</div>
      <div class="feat" style="font-size:3.5px"><svg width="12" height="10" viewBox="0 0 18 14"><path d="M1 13 L17 9 M5 11 L9 3 L13 10" fill="none" stroke="#9db0e0" stroke-width="1.4"/><circle cx="9" cy="2" r="1.6" fill="#9db0e0"/></svg>Certified<br>instructors</div>
      <div class="feat" style="font-size:3.5px"><svg width="12" height="10" viewBox="0 0 18 14"><path d="M1 13 L17 9 M5 11 L9 3 L13 10" fill="none" stroke="#9db0e0" stroke-width="1.4"/><circle cx="9" cy="2" r="1.6" fill="#9db0e0"/></svg>Affordable<br>pricing</div>
    </div>
    <p class="abs copy" style="left:12px;width:128px;top:335px;font-size:4px">Lorem ipsum dolor sit amet, consectetur adipiscing elit, sed do eiusmod tempor incididunt ut labore et dolore magna aliqua. Quis ipsum suspendisse ultrices.</p>
  </section>

  <section class="sec testi" style="top:717px;height:498px">
    <p class="abs center kicker" style="top:36px;font-size:4px;letter-spacing:1.5px">Places to visit</p>
    <h2 class="abs center head" style="top:48px;font-size:11px">Tour skiing places</h2>
    <p class="abs copy" style="left:14px;width:123px;top:74px;font-size:4px;text-align:center">Lorem ipsum dolor sit amet, consectetur adipiscing elit, sed do eiusmod tempor incididunt ut labore et dolore.</p>
    <div class="photo card-img" role="img" aria-label="Snowy forest at Castle" style="left:9px;top:119px;width:133px;height:94px"></div>
    <div class="abs card-label" style="left:20px;top:197px;width:111px;height:26px;font-size:5px">Castle</div>
    <div class="photo card-img" role="img" aria-label="Snow-capped Electric Peak" style="left:9px;top:238px;width:133px;height:94px;background:linear-gradient(180deg,#4d7cc9 0%,#a9c2ea 40%,#eef2f8 70%,#b6c3d6 100%)"></div>
    <div class="abs card-label" style="left:20px;top:316px;width:111px;height:26px;font-size:5px">Electric Peak</div>
    <div class="photo card-img" role="img" aria-label="Forest trail at Mineral Hill" style="left:9px;top:356px;width:133px;height:94px;background:linear-gradient(180deg,#9fb7e2 0%,#4d5a4f 40%,#e8ecf2 85%)"></div>
    <div class="abs card-label" style="left:20px;top:434px;width:111px;height:26px;font-size:5px">Mineral Hi</div>
  </section>

  <section class="sec book" role="img" aria-label="Snow-covered spruce trees on a white hillside" style="top:1215px;height:235px">
    <h2 class="abs head" style="left:9px;top:33px;font-size:11px;font-weight:400;line-height:1.45">Book your tour<br>now and have an<br>amazing experience</h2>
    <p class="abs copy" style="left:9px;width:130px;top:100px;font-size:3.8px">Lorem ipsum dolor sit amet, consectetur adipiscing elit, sed do eiusmod tempor incididunt ut labore et dolore magna aliqua. Quis ipsum suspendisse ultrices gravida.</p>
    <p class="abs copy" style="left:9px;width:130px;top:143px;font-size:3.8px">Lorem ipsum dolor sit amet, consectetur adipiscing elit, sed do eiusmod tempor incididunt.</p>
    <div class="abs btn" style="left:9px;top:181px;width:38px;height:18px;font-size:3.5px">Book Tour</div>
  </section>

  <section class="sec" style="top:1450px;height:648px">
    <p class="abs center kicker" style="top:33px;font-size:4px;letter-spacing:1.5px">Recent posts</p>
    <h2 class="abs center head" style="top:45px;font-size:11px">Gallery</h2>
    <div class="photo g1" role="img" aria-label="Dark pines against misty light" style="left:10px;top:79px;width:130px;height:79px"></div>
    <div class="photo g4" role="img" aria-label="Foggy blue winter forest" style="left:10px;top:168px;width:130px;height:80px"></div>
    <div class="photo g2" role="img" aria-label="Tall snowy pines beside a trail" style="left:10px;top:259px;width:130px;height:171px"></div>
    <div class="photo g3" role="img" aria-label="Frosted trees on an open snowfield" style="left:10px;top:440px;width:130px;height:80px"></div>
    <div class="photo g5" role="img" aria-label="Aerial view of a road through snowy forest" style="left:10px;top:531px;width:130px;height:79px"></div>
  </section>

  <section class="sec call" style="top:2098px;height:129px">
    <h2 class="abs center head" style="top:30px;font-size:11px;font-weight:400">Call us now at<br>+1 234 567 890</h2>
    <p class="abs copy" style="left:12px;width:127px;top:68px;font-size:3.8px;text-align:center">Lorem ipsum dolor sit amet, consectetur adipiscing elit, sed do eiusmod tempor incididunt ut labore.</p>
  </section>

  <section class="sec testi" style="top:2227px;height:171px">
    <p class="abs center kicker" style="top:31px;font-size:4px;letter-spacing:1.5px">What our clients say</p>
    <h2 class="abs center head" style="top:43px;font-size:11px">Testimonials</h2>
    <p class="abs copy" style="left:14px;width:123px;top:70px;font-size:3.8px;text-align:center">Lorem ipsum dolor sit amet, consectetur et nisl adipiscing elit, sed do eiusmod tempor incididunt ut labore et dolore magna aliqua.</p>
    <div class="abs avatar" role="img" aria-label="Client portrait" style="left:68px;top:118px;width:15px;height:15px"></div>
    <p class="abs center name" style="top:139px;font-size:4px">Dana Holloway</p>
  </section>

  <section class="sec save" style="top:2398px;height:195px">
    <h2 class="abs center head" style="top:41px;font-size:11px">Save up to 30%<br>at early winter</h2>
    <p class="abs copy" style="left:14px;width:123px;top:88px;font-size:3.8px;text-align:center">Lorem ipsum dolor sit amet, consectetur adipiscing elit, sed do eiusmod tempor incididunt ut labore et dolore.</p>
    <div class="abs btn" style="left:48px;top:132px;width:55px;height:21px;font-size:3.8px">Learn More</div>
  </section>

  <footer class="sec footer" style="top:2593px;height:152px">
    <span class="abs logo-dot" style="left:57px;top:32px;width:37px;height:37px"></span>
    <div class="abs contact" style="left:0;right:0;top:89px;font-size:3.5px;gap:8px"><span>+1 234 567 890</span><span>hello@fernwickridge.test</span></div>
    <div class="abs socials" style="left:0;right:0;top:114px;gap:5px"><span style="width:6px;height:6px"></span><span class="on" style="width:6px;height:6px"></span><span style="width:6px;height:6px"></span></div>
  </footer>
  <div class="sec copyright" style="top:2745px;height:19px;font-size:3px">Copyright 2021 © Fernwick Ridge Glide Treks - All rights reserved</div>
</main>

</body>
</html>
```